Webdesign für Getränkesofortlieferant
Zielgruppe
kistenbote ist ein Getränkesofortlieferant. Wir suchen ein hochwertiges Design für unsere Jobwebseite. Unsere Zielgruppe sind daher alle Bewerber, die sich für Jobs im Lager/in der Auslieferung interessieren sowie Bewerber, die sich für Jobs im Headquarter interessieren (z.B. im Marketing, in der IT, Finance etc.).
Aufgabenstellung
siehe Anhang

```html
<!DOCTYPE html>
<html lang="de">
<head>
<meta charset="utf-8">
<title>kistenbote Jobs</title>
<link href="https://fonts.googleapis.com/css2?family=Montserrat:wght@400;500;700&family=Roboto:wght@300;400;500;700&display=swap" rel="stylesheet">
<style>
:root{
  --dark:#333333;
  --dark2:#3b3b3b;
  --green:#8aa824;
  --green-light:#a4c232;
  --magenta:#c2187a;
  --purple:#8a2a6e;
  --blue:#175c93;
  --pink:#e8579e;
  --white:#ffffff;
}
*{margin:0;padding:0;box-sizing:border-box}
html,body{width:1200px;height:2749px;overflow:hidden}
body{font-family:'Montserrat',sans-serif;background:var(--dark);color:var(--white);position:relative}
.abs{position:absolute}
/* header */
.site-header{position:absolute;top:0;left:0;width:1200px;height:72px;background:var(--dark);z-index:5}
.brand{position:absolute;left:272px;top:2px;width:116px;height:116px;border-radius:50%;background:var(--green);border:5px solid var(--green-light);display:flex;align-items:center;justify-content:center;font-family:'Roboto',sans-serif;font-weight:700;font-size:18px;color:var(--white)}
.nav-item{position:absolute;top:0;height:72px;display:flex;flex-direction:column;align-items:center;justify-content:center;gap:8px;font-family:'Roboto',sans-serif;font-size:17px;color:#eee;text-transform:uppercase}
.nav-item svg{width:18px;height:18px}
.nav-item.active{background:var(--purple)}
/* hero */
.hero{top:72px;left:0;width:1200px;height:572px;background:linear-gradient(100deg,#8a7b63 0%,#c9b99b 30%,#9b9184 55%,#6d6a69 80%,#55504c 100%)}
.hero-arrow{top:245px;width:68px;height:130px;background:rgba(40,40,40,.75);display:flex;align-items:center;justify-content:center}
.hero-title{left:200px;top:340px;width:293px;height:138px;background:rgba(40,40,40,.85);padding:28px 8px 0 22px;font-family:'Roboto',sans-serif;color:var(--green-light);line-height:1.15;white-space:nowrap}
.hero-title .thin{font-weight:300;font-size:34px;display:block}
.hero-title .bold{font-weight:700;font-size:37px;display:block;margin-top:4px}
.hero-copy{left:493px;top:340px;width:572px;height:138px;background:rgba(40,40,40,.85);padding:18px 22px;font-size:16.5px;line-height:26px;color:#f2f2f2}
.hero-cta{left:493px;top:478px;width:572px;height:46px;background:var(--green);display:flex;align-items:center;justify-content:space-between;padding:0 24px;font-family:'Roboto',sans-serif;font-weight:700;font-size:17px;color:#1c1c1c}
.hero-dots{top:619px;left:520px;display:flex;gap:12px}
.hero-dots span{width:28px;height:3px;background:#333;display:block}
/* timeline */
.timeline{top:644px;left:0;width:1200px;height:676px;background:var(--dark2)}
.section-title{font-weight:700;font-size:32px;color:var(--white);text-align:center}
.section-title::after{content:"";display:block;width:66px;height:3px;background:var(--green);margin:6px auto 0}
.map-area{left:90px;top:160px;width:370px;height:470px;border-radius:40% 40% 30% 30%;background:radial-gradient(ellipse at 50% 45%,#d8d8d8 0%,#bdbdbd 55%,rgba(59,59,59,0) 72%)}
.road{left:855px;top:44px;width:42px;height:577px}
.tl-box{height:54px;border-radius:6px;display:flex;align-items:center;padding:0 14px;font-family:'Roboto',sans-serif;font-size:17px;color:var(--white)}
.tl-year{font-weight:700;font-size:30px;color:var(--white)}
.tl-dot{width:40px;height:40px;border-radius:50%;border:3px solid #fff;display:flex;align-items:center;justify-content:center}
/* locations */
.locations-photo{top:1320px;left:0;width:1200px;height:615px;background:linear-gradient(95deg,#6a8d8a 0%,#9aa4a6 30%,#54524f 55%,#3a3a40 65%,#c2187a 75%,#d46aa8 100%)}
.locations-label{left:480px;top:1768px;width:260px;height:96px;background:rgba(255,255,255,.55);display:flex;flex-direction:column;align-items:center;justify-content:center;font-weight:700;font-size:32px;line-height:36px;color:var(--magenta);text-align:center}
.locations-label::after{content:"";width:110px;height:3px;background:#1c1c1c;margin-top:4px}
.carousel{top:1935px;left:0;width:1200px;height:240px;background:var(--white)}
.loc-card{top:20px;width:302px;height:198px;border:4px solid #eee;box-shadow:0 1px 4px rgba(0,0,0,.3)}
.loc-card .pic{position:absolute;inset:0}
.loc-card .cap{position:absolute;left:6px;right:6px;bottom:4px;height:34px;background:var(--purple);display:flex;align-items:center;justify-content:center;font-weight:700;font-size:17px}
/* facts */
.facts{top:2175px;left:0;width:1200px;height:505px;background:var(--dark)}
.fact{width:280px;text-align:center}
.fact-ring{width:184px;height:184px;border-radius:50%;border:2px dashed #4a4a4a;margin:0 auto;display:flex;align-items:center;justify-content:center}
.fact-num{font-weight:700;font-size:38px;line-height:40px;margin-top:42px}
.fact-label{font-size:14px;margin-top:6px}
.fact-pre{font-size:13px;line-height:16px;position:absolute;left:0;right:0;top:208px}
/* footer */
.site-footer{top:2680px;left:0;width:1200px;height:69px;border-top:1px solid #555;background:var(--dark);font-size:12px;display:flex;align-items:center;padding-left:71px;color:#eee}
.site-footer span{margin-right:16px}
.social{width:50px;height:34px;border-radius:6px;display:flex;align-items:center;justify-content:center;font-size:9px;font-weight:700}
</style>
</head>
<body>

<header class="site-header">
  <div class="brand">kistenbote</div>
  <div class="nav-item" style="left:420px;width:145px">
    <svg viewBox="0 0 18 18" fill="#ddd"><rect x="2" y="3" width="14" height="13"/><g fill="#333"><rect x="4" y="5" width="2" height="2"/><rect x="8" y="5" width="2" height="2"/><rect x="12" y="5" width="2" height="2"/><rect x="4" y="9" width="2" height="2"/><rect x="8" y="9" width="2" height="2"/><rect x="12" y="9" width="2" height="2"/><rect x="8" y="13" width="2" height="3"/></g></svg>
    <span>Unternehmen</span></div>
  <div class="nav-item active" style="left:614px;width:128px">
    <svg viewBox="0 0 18 18" fill="#ddd"><rect x="1" y="5" width="16" height="11" rx="1"/><rect x="6" y="2" width="6" height="4" fill="none" stroke="#ddd" stroke-width="2"/><circle cx="9" cy="10" r="3" fill="#8a2a6e"/></svg>
    <span>Jobs</span></div>
  <div class="nav-item" style="left:770px;width:92px">
    <svg viewBox="0 0 18 18" fill="#ddd"><rect x="3" y="1" width="12" height="16"/><g fill="#333"><rect x="5" y="4" width="8" height="1.5"/><rect x="5" y="8" width="8" height="1.5"/><rect x="5" y="12" width="8" height="1.5"/></g></svg>
    <span>FAQ</span></div>
  <div class="nav-item" style="left:1060px;width:120px">
    <svg viewBox="0 0 18 18" fill="#ddd"><path d="M1 2h3l2 9h9l2-7H5" fill="none" stroke="#ddd" stroke-width="2"/><circle cx="7" cy="15" r="1.6"/><circle cx="14" cy="15" r="1.6"/></svg>
    <span>Unser Shop</span></div>
</header>

<section class="abs hero" role="img" aria-label="Fahrer mit Sackkarre und Getränkekisten in einer Altstadtstraße, Lieferwagen im Hintergrund"></section>
<div class="abs hero-arrow" style="left:0"><svg width="30" height="50" viewBox="0 0 30 50"><path d="M28 2 2 25l26 23z" fill="#eee"/></svg></div>
<div class="abs hero-arrow" style="left:1132px"><svg width="30" height="50" viewBox="0 0 30 50"><path d="M2 2l26 23L2 48z" fill="#eee"/></svg></div>
<div class="abs hero-title"><span class="thin">GETRÄNKE FÜR</span><span class="bold">ALLE. SOFORT.</span></div>
<div class="abs hero-copy">Der Wasservorrat für das Büro, das Bier für den Grillabend oder die Cola für zwischendurch - wir liefern innerhalb von 120 Minuten. Und das alles egal in welches Stockwerk, ohne Liefergebühr und zu Preisen wie im Supermarkt.</div>
<div class="abs hero-cta"><span>LASST UNS DEN GETRÄNKEHANDEL REVOLUTIONIEREN!</span>
  <svg width="36" height="20" viewBox="0 0 36 20"><path d="M2 2l10 8-10 8M14 2l10 8-10 8M24 2l10 8-10 8" fill="none" stroke="#1c1c1c" stroke-width="4"/></svg></div>
<div class="abs hero-dots"><span></span><span></span><span></span></div>

<section class="abs timeline">
  <h2 class="abs section-title" style="left:220px;top:56px;width:200px">TIMELINE</h2>
  <div class="abs map-area" role="img" aria-label="Deutschlandkarte mit Standortpunkten und Lieferwagen"></div>
  <svg class="abs road" viewBox="0 0 42 577">
    <path d="M21 0 42 22H0z" fill="#888"/>
    <rect x="0" y="24" width="42" height="528" fill="#1d1d1d"/>
    <line x1="21" y1="30" x2="21" y2="548" stroke="#888" stroke-width="2" stroke-dasharray="14 12"/>
    <path d="M0 555h42L21 577z" fill="#888"/>
  </svg>
  <p class="abs" style="left:588px;top:138px;width:250px;text-align:center;font-size:14px;line-height:16px">Expansion Mannheim/Heidelberg, Ludwigshafen und Düsseldorf<br>(evtl. auf Monate aufgeteilt)</p>
  <div class="abs tl-dot" style="left:856px;top:146px;background:var(--pink)"><svg width="20" height="20" viewBox="0 0 20 20"><circle cx="10" cy="10" r="8" fill="none" stroke="#fff" stroke-width="2"/></svg></div>
  <div class="abs tl-box" style="left:929px;top:139px;width:194px;background:var(--pink);line-height:20px">Bald auch in<br>deiner Stadt?</div>
  <svg class="abs" style="left:915px;top:156px" width="14" height="20"><path d="M14 0v20L0 10z" fill="#e8579e"/></svg>

  <div class="abs tl-year" style="left:631px;top:230px">2018</div>
  <div class="abs tl-box" style="left:628px;top:268px;width:196px;background:var(--blue)">Expansion Mannheim</div>
  <svg class="abs" style="left:824px;top:285px" width="14" height="20"><path d="M0 0v20l14-10z" fill="#175c93"/></svg>
  <div class="abs tl-dot" style="left:856px;top:275px;background:var(--blue)"><svg width="20" height="20" viewBox="0 0 20 20"><rect x="2" y="3" width="16" height="14" fill="none" stroke="#fff" stroke-width="2"/><line x1="2" y1="7" x2="18" y2="7" stroke="#fff" stroke-width="2"/></svg></div>

  <div class="abs tl-year" style="left:1050px;top:362px">2017</div>
  <div class="abs tl-dot" style="left:856px;top:403px;background:var(--magenta)"><svg width="20" height="20" viewBox="0 0 20 20"><path d="M3 12l10-8v14z" fill="#fff"/></svg></div>
  <svg class="abs" style="left:915px;top:413px" width="14" height="20"><path d="M14 0v20L0 10z" fill="#c2187a"/></svg>
  <div class="abs tl-box" style="left:929px;top:396px;width:194px;background:var(--magenta);justify-content:center">Expansion Köln</div>

  <div class="abs tl-year" style="left:634px;top:485px">2016</div>
  <div class="abs tl-box" style="left:628px;top:520px;width:196px;background:var(--green)">Gründung in Münster</div>
  <svg class="abs" style="left:824px;top:537px" width="14" height="20"><path d="M0 0v20l14-10z" fill="#8aa824"/></svg>
  <div class="abs tl-dot" style="left:856px;top:527px;background:var(--green)"><svg width="20" height="20" viewBox="0 0 20 20"><path d="M4 2v16M4 3h12l-3 4 3 4H4" fill="#fff" stroke="#fff" stroke-width="2"/></svg></div>
</section>

<section class="abs locations-photo" role="img" aria-label="Mitarbeiterin lädt Getränkekisten im Lager in einen magentafarbenen Lieferwagen"></section>
<h2 class="abs locations-label">UNSERER<br>STANDORTE</h2>

<section class="abs carousel">
  <svg class="abs" style="left:52px;top:65px" width="44" height="100" viewBox="0 0 44 100"><path d="M40 0 4 50l36 50h-12L0 50 28 0z" fill="#8aa824"/></svg>
  <div class="abs loc-card" style="left:122px"><div class="pic" role="img" aria-label="Lagergebäude mit Lieferwagenflotte" style="background:linear-gradient(180deg,#8da1b4,#b9bfc6 60%,#9a9a9a)"></div><div class="cap">Standort Münster</div></div>
  <div class="abs loc-card" style="left:459px"><div class="pic" role="img" aria-label="Mitarbeiter in Warnwesten im Getränkelager" style="background:linear-gradient(180deg,#6b6c5e,#a09a74 55%,#7a7966)"></div><div class="cap">Standort Köln</div></div>
  <div class="abs loc-card" style="left:794px"><div class="pic" role="img" aria-label="Große Lagerhalle mit gestapelten Getränkekisten" style="background:linear-gradient(180deg,#a6a8aa,#5c6f7c 50%,#7b6a4a)"></div><div class="cap">Standort Düsseldorf</div></div>
  <svg class="abs" style="left:1108px;top:65px" width="44" height="100" viewBox="0 0 44 100"><path d="M4 0l36 50-36 50h12l28-50L16 0z" fill="#8aa824"/></svg>
</section>

<section class="abs facts">
  <h2 class="abs section-title" style="left:500px;top:52px;width:200px">FAKTEN</h2>
  <div class="abs fact" style="left:170px;top:150px">
    <div class="fact-ring"><svg width="120" height="100" viewBox="0 0 120 100" fill="none" stroke="#8aa824" stroke-width="5"><rect x="40" y="40" width="72" height="48"/><path d="M56 40V20h8v20M90 40V20h8v20M10 50l40 40"/></svg></div>
    <div class="fact-num">15.000</div><div class="fact-label">Ausgelieferte Kisten am Tag</div></div>
  <div class="abs fact" style="left:460px;top:150px">
    <div class="fact-ring" style="background:#111;border:3px solid #555"><svg width="120" height="90" viewBox="0 0 120 90" fill="none" stroke="#8aa824" stroke-width="5"><rect x="18" y="10" width="84" height="56"/><path d="M8 76h104"/><circle cx="60" cy="38" r="16"/></svg></div>
    <div class="fact-num">1.200.000</div><div class="fact-label">Bestellungen pro Jahr</div></div>
  <div class="abs fact" style="left:727px;top:150px">
    <div class="fact-ring"><svg width="140" height="100" viewBox="0 0 140 100" fill="none" stroke="#8aa824" stroke-width="5"><path d="M70 95 48 50a22 22 0 1 1 44 0z"/><path d="M22 85 8 60a14 14 0 1 1 28 0z"/><path d="M118 85 104 60a14 14 0 1 1 28 0z"/></svg></div>
    <div class="fact-pre">Bis zu</div>
    <div class="fact-num">500</div><div class="fact-label">Motivierte Mitarbeiter pro Standort</div></div>
</section>

<footer class="abs site-footer">
  <span>Copyright kistenbote GmbH</span><span>|</span><span>DATENSCHUTZ</span><span>|</span><span>IMPRESSUM</span>
  <div class="abs social" style="left:946px;top:17px;background:#555">Socialo</div>
  <div class="abs social" style="left:1006px;top:17px;background:var(--magenta)">Bildwerk</div>
</footer>

</body>
</html>
```